Business Card Design

We require a business card design for a law firm, our signature colours are maroon and cream. Our slogan is "From our family to yours", we would like the cards to be professional however feminine at the same time.

Industry/Entity Type

Business

Contact Information for Business Card

Helena Brackett & Associates Lawyers & Conveyancers, Helena Brackett LL.B. Principal Solicitor, 17 Quillon Street, Marrowdale NSW 2190

Logo styles of interest
Emblem Logo
Abstract Logo
Wordmark Logo

```html
<!DOCTYPE html>
<html lang="en">
<head>
<meta charset="utf-8">
<title>Helena Brackett &amp; Associates – Business Card</title>
<link rel="stylesheet" href="https://fonts.googleapis.com/css2?family=Libre+Baskerville:wght@400;700&family=Lato:wght@400;700&display=swap">
<style>
  :root {
    --backdrop: #1c1c1e;
    --maroon: #74191c;
    --maroon-deep: #5e1214;
    --cream: #efe3b0;
    --cream-soft: #e8d99c;
  }
  * { margin: 0; padding: 0; box-sizing: border-box; }
  html, body {
    width: 1200px; height: 1000px; overflow: hidden;
    background: var(--backdrop);
  }
  .card {
    position: absolute; left: 100px; top: 215px;
    width: 1000px; height: 570px;
    background: linear-gradient(160deg, var(--maroon) 0%, var(--maroon-deep) 100%);
    color: var(--cream);
    font-family: "Lato", sans-serif;
  }
  .wordmark {
    position: absolute; left: 90px; top: 120px; width: 340px;
    display: flex; flex-direction: column; align-items: center; gap: 22px;
    font-family: "Libre Baskerville", serif; font-weight: 400;
    color: var(--cream); text-align: center;
  }
  .wordmark-dot {
    width: 72px; height: 72px; border-radius: 50%;
    border: 3px solid var(--cream);
  }
  .wordmark-name { font-size: 24px; line-height: 1.35; }
  .firm-tagline {
    position: absolute; right: 60px; top: 50px;
    text-align: right; font-weight: 700; font-size: 17px; line-height: 1.3;
  }
  .person {
    position: absolute; left: 90px; top: 400px;
  }
  .person-name {
    font-family: "Libre Baskerville", serif; font-weight: 700;
    font-size: 30px; color: var(--cream-soft);
  }
  .person-title { font-size: 22px; margin-top: 8px; }
  .divider {
    position: absolute; left: 520px; top: 370px;
    width: 2px; height: 120px; background: var(--cream);
  }
  .contacts {
    position: absolute; right: 50px; top: 355px;
    list-style: none; font-size: 17px; line-height: 1.55; text-align: right;
  }
  .contacts li { display: flex; justify-content: flex-end; align-items: center; gap: 6px; }
  .contacts svg { width: 16px; height: 16px; fill: var(--cream); }
</style>
</head>
<body>
  <section class="card" aria-label="Business card">
    <div class="wordmark">
      <span class="wordmark-dot" aria-hidden="true"></span>
      <span class="wordmark-name">Helena Brackett &amp; Associates Lawyers</span>
    </div>

    <p class="firm-tagline">
      Helena Brackett &amp; Associates Lawyers<br>
      &amp; Conveyancers<br>
      "From our family to yours"
    </p>

    <div class="person">
      <p class="person-name">Helena Brackett LL.B</p>
      <p class="person-title">Principal Solicitor</p>
    </div>

    <span class="divider" aria-hidden="true"></span>

    <ul class="contacts">
      <li>000.5550.142 :
        <svg viewBox="0 0 16 16" aria-hidden="true"><path d="M2 5c2-3 10-3 12 0l-2 2-2-1V5H6v1L4 7 2 5zM4 8h8l2 6H2l2-6zm4 1.5a2 2 0 100 4 2 2 0 000-4z"/></svg>
      </li>
      <li>helenabrackett@brackettlawyers.com :
        <svg viewBox="0 0 16 16" aria-hidden="true"><path d="M1 3h14v10H1V3zm1.5 1.2L8 8.5l5.5-4.3V12h-11V4.2z"/></svg>
      </li>
      <li>www.helenabrackettassociates.com :
        <svg viewBox="0 0 16 16" aria-hidden="true"><path d="M8 1a7 7 0 110 14A7 7 0 018 1zm-5.4 6h2.3c.1-1.8.5-3.2 1.1-4.2A5.5 5.5 0 002.6 7zm0 2a5.5 5.5 0 003.4 4.2C5.4 12.2 5 10.8 4.9 9H2.6zm3.8 0c.1 2.4.9 4 1.6 4.4.7-.4 1.5-2 1.6-4.4H6.4zm0-2h3.2C9.5 4.6 8.7 3 8 2.6 7.3 3 6.5 4.6 6.4 7zm4.7 0h2.3a5.5 5.5 0 00-3.4-4.2c.6 1 1 2.4 1.1 4.2zm2.3 2h-2.3c-.1 1.8-.5 3.2-1.1 4.2A5.5 5.5 0 0013.4 9z"/></svg>
      </li>
      <li>17 Quillon Street, Marrowdale NSW 2190 :
        <svg viewBox="0 0 16 16" aria-hidden="true"><path d="M8 1a5 5 0 015 5c0 3.5-5 9-5 9S3 9.5 3 6a5 5 0 015-5zm0 3a2 2 0 100 4 2 2 0 000-4z"/></svg>
      </li>
    </ul>
  </section>
</body>
</html>
```